Corporate brochure for a multinational construction company

Designing the cover pages and inside pages layout for a construction company which has operations in GCC, India etc. It has to be a very classy design. you can visit our website www.belvorant.com for more details on the company. Specific information required for the brochure design will be uploaded as needed.

Please note
1. Though the brochure will be around 80 pages, we need design of only the following
a. Cover page
b. CEOs message page
c. Introduction to sectors (Civil, Electrical, Mechanical, Infra)
d. Pages showing engineering expertise
e. Pages showing Project highlights (buildings etc)
f. Gallery pages (2 to 4 images in each page showing completed projects with a small text)
g. Key personnel (images and positions of key staff)

So design has to be done for a maximum of 7 to 10 pages. rest will be repetition.
Please use stock images with the above tip and send your designs.
g.
Updates

Project Deadline Extended
Reason: Not happy with the designs provided till now. Request all designers to once again look at the brief which is updated and submit maximum revisions. The pay is committed so we will select the best in any case. wish you all the best.

Target Market(s)

International - Current operations in the GCC, India, Srilanka

Industry/Entity Type

Construction Company

Font styles to use
Serif
Sans Serif

Requirements
Must have
• 1. A great front cover design - this may run to the back cover also
• 2. Inside page layout - to have a common theme but different styling as required
• 3. More of images and less of text - can use full page, half page or quarter page images.
• 4. Different styling and sizes for fonts for better effect.
Nice to have
• 1. A4 landscape is what we have in mind. The size can be slightly reduced so that the 80 page brochure can fit into an A4 envelope

```html
<!DOCTYPE html>
<html lang="en">
<head>
<meta charset="utf-8">
<title>Belvorant Brochure – Inside Spreads</title>
<link href="https://fonts.googleapis.com/css2?family=Libre+Baskerville:wght@400;700&family=Open+Sans:wght@400;600&display=swap" rel="stylesheet">
<style>
  :root{
    --bg:#e4e5e8;
    --charcoal:#2b2c2e;
    --charcoal-soft:#333436;
    --blue:#5b8fc9;
    --blue-deep:#3f6fa8;
    --blue-light:#8fb4dd;
    --panel-blue:rgba(40,76,132,.9);
    --panel-dark:rgba(40,40,42,.9);
    --paper:#f1f2f3;
    --ink:#2a2a2a;
    --white:#ffffff;
  }
  *{margin:0;padding:0;box-sizing:border-box}
  html,body{width:1200px;height:1200px;overflow:hidden;background:var(--bg)}
  .canvas{position:relative;width:1200px;height:1200px}
  .spread{position:absolute;width:784px;height:278px;display:flex;box-shadow:0 12px 26px rgba(0,0,0,.22)}
  .spread--projects{top:176px;left:202px}
  .spread--gallery{top:778px;left:212px;width:780px}
  .page{position:relative;width:50%;height:278px;overflow:hidden}
  .photo{position:absolute}
  .photo--white-arches{background:linear-gradient(172deg,#3f86dc 0%,#8cbcec 12%,#f7f6f1 20%,#eef0ee 34%,#3f76c4 40%,#f3f2ec 46%,#eceae2 58%,#2f63a8 64%,#e9e6dc 72%,#44603a 84%,#2c3d24 92%,#4c4a44 100%)}
  .photo--palm-office{background:linear-gradient(180deg,#1f5fc4 0%,#3d82dc 22%,#6ea7e6 40%,#f1ead2 48%,#e9e0c2 62%,#d8cdab 78%,#5f6a42 86%,#a39d8c 92%,#6d695f 100%)}
  .photo--sand-facade{background:linear-gradient(180deg,#b5d3ee 0%,#c9dcec 12%,#c9946a 20%,#d8a979 45%,#bb8458 62%,#c8a582 78%,#e8dfcf 88%,#d9d0bd 100%)}
  .photo--flag-building{background:linear-gradient(180deg,#4f93dd 0%,#8dbbea 30%,#c9a24f 38%,#d7ae58 55%,#b88d3d 70%,#e8e6e2 78%,#8d8c88 88%,#bdbbb6 100%)}
  .full{left:0;top:0;width:100%;height:100%}
  .running-head{position:absolute;top:26px;right:10px;font:400 6px/1 "Libre Baskerville",serif;color:var(--ink);display:flex;align-items:center;gap:6px;white-space:nowrap}
  .running-head--light{color:var(--white)}
  .running-head .rule{display:block;width:136px;height:2px;background:var(--blue)}
  .running-head .rule--dark{background:#23324a}
  .feature-box{position:absolute;top:122px;width:140px;height:124px;padding:15px 11px 0}
  .feature-box--blue{left:219px;background:var(--panel-blue)}
  .feature-box--dark{left:42px;background:var(--panel-dark)}
  .feature-title{font:400 15px/1.12 "Libre Baskerville",serif;color:var(--white)}
  .feature-underline{width:58px;height:2px;background:var(--blue);margin:4px 0 10px}
  .feature-text{font:400 5.2px/1.55 "Open Sans",sans-serif;color:var(--white)}
  .folio{position:absolute;font:400 7px/1 "Libre Baskerville",serif;color:var(--ink)}
  .folio--light{color:#6a6a6c}
  .page--light{background:linear-gradient(90deg,#fafafa 0%,var(--paper) 70%,#d9dadb 100%)}
  .page--dark{background:var(--charcoal-soft)}
  .gallery-title{position:absolute;top:68px;font:400 15px/1 "Libre Baskerville",serif;color:var(--ink)}
  .gallery-title--light{color:var(--white)}
  .gallery-title::after{content:"";display:block;width:58px;height:2px;background:var(--blue);margin-top:5px}
  .bottom-rule{position:absolute;bottom:25px;height:1px;background:#8e8f91}
  .deco{position:absolute;left:0;top:0}
</style>
</head>
<body>
<main class="canvas">

  <section class="spread spread--projects">
    <article class="page">
      <div class="photo photo--white-arches full" role="img" aria-label="White arched commercial building with blue glazing and palm trees"></div>
      <svg class="deco" width="100" height="278" viewBox="0 0 100 278">
        <polygon points="0,0 14,0 14,200 0,220" fill="var(--charcoal)"/>
        <polygon points="14,0 60,0 14,90" fill="var(--blue-deep)"/>
        <polygon points="40,0 86,0 52,60" fill="var(--blue-light)"/>
        <polygon points="14,90 60,0 64,36 14,190" fill="var(--blue)"/>
      </svg>
      <p class="running-head running-head--light">Belvorant Trading &amp; Construction LLC Oman</p>
      <div class="feature-box feature-box--blue">
        <h2 class="feature-title">Commercial<br>Buildings</h2>
        <div class="feature-underline"></div>
        <p class="feature-text">Belvorant, as an EPC company with more than 3 decades of experience in Oman has built landmarks around the country in almost all sectors.</p>
      </div>
    </article>
    <article class="page">
      <div class="photo photo--palm-office full" role="img" aria-label="Cream office building with palm trees and flags under blue sky"></div>
      <p class="running-head running-head--light"><span class="rule rule--dark"></span>Belvorant Trading &amp; Construction LLC Oman</p>
      <div class="feature-box feature-box--dark">
        <h2 class="feature-title">Commercial<br>Buildings</h2>
        <div class="feature-underline"></div>
        <p class="feature-text">Belvorant, as an EPC company with more than 3 decades of experience in Oman has built landmarks around the country in almost all sectors.</p>
      </div>
      <span class="folio" style="left:46px;bottom:16px">28</span>
    </article>
  </section>

  <section class="spread spread--gallery">
    <article class="page page--light">
      <svg class="deco" width="100" height="278" viewBox="0 0 100 278">
        <polygon points="0,0 12,0 12,230 0,250" fill="var(--charcoal)"/>
        <polygon points="12,0 58,0 12,88" fill="var(--blue-deep)"/>
        <polygon points="36,0 86,0 52,56" fill="var(--blue-light)"/>
        <polygon points="12,88 58,0 62,40 12,220" fill="var(--blue)"/>
      </svg>
      <p class="running-head"><span class="rule"></span>Belvorant Trading &amp; Construction LLC Oman</p>
      <h2 class="gallery-title" style="left:68px">Gallery</h2>
      <div class="photo photo--palm-office" style="left:41px;top:105px;width:152px;height:132px" role="img" aria-label="Cream office building with palm trees"></div>
      <div class="photo photo--white-arches" style="left:195px;top:105px;width:152px;height:132px" role="img" aria-label="White arched commercial building entrance"></div>
      <div class="bottom-rule" style="left:20px;right:36px"></div>
      <span class="folio" style="right:36px;bottom:14px">46</span>
    </article>
    <article class="page page--dark">
      <p class="running-head running-head--light"><span class="rule"></span>Belvorant Trading &amp; Construction LLC Oman</p>
      <h2 class="gallery-title gallery-title--light" style="left:44px">Gallery</h2>
      <div class="photo photo--sand-facade" style="left:38px;top:105px;width:152px;height:132px" role="img" aria-label="Sand coloured building with patterned facade"></div>
      <div class="photo photo--flag-building" style="left:193px;top:105px;width:152px;height:132px" role="img" aria-label="Ochre government building with flags"></div>
      <svg class="deco" width="390" height="278" viewBox="0 0 390 278">
        <polygon points="345,194 390,194 390,278" fill="var(--blue)"/>
        <polygon points="345,194 372,194 390,250" fill="var(--blue-deep)" opacity=".6"/>
      </svg>
      <div class="bottom-rule" style="left:44px;right:14px;background:#5c5d60"></div>
      <span class="folio folio--light" style="left:50px;bottom:14px">47</span>
    </article>
  </section>

</main>
</body>
</html>
```